Australian Online Training Organisation needs a Website Design

We need a Web Design ideally using a Wordpress Divi template which will represent an Australian Online Training Company.

(Harlow Net Learning)

The website will represent a range of short courses with an emphasis on business, zentrosoft, leadership etc.

The website will 'shell out' to the third party portal where 'bookings' occur. I am imaging a fantastic looking web design with perhaps 5-6 pages.

I am wondering if a selection of courses including the below list can be incorporated?

The variety of courses include :

Workplace Safety
Sales Training
Leadership
Process Management
Problem Solving
Project Management
Business Planning
Meetings and Events
Emotional Intelligence
Human Resources
Administrative Essentials
Customer Service
Career Development
Conflict Resolution
Train the Trainer
Supervisors and Managers
Internet marketing
Communications
Team Building
Marketing
Finance
Writing
Job Search Skills
Public Speaking
Negotiation Skills
Talent Management
Zentrosoft Deskline 2016
ZDC Preparation for Office 2010
Office 2013
Office 2010
Upgrading to Office 2010
Computer Fundamentals
Upgrading to Office 2007
Office 2003
Office 2002
Pavra Suite X3
Core Essentials
Office 2007

Thank you so much for all of the amazing designs we received. We were so happy with so many elements that it was very hard to choose. Our top two were very hard to decide upon but we look forward to working more with both of these talents into the future. Thank you again.

Target Market(s)

Professionals, students and workers who would like to improve their skills with online training in over 500 + courses -

Industry/Entity Type

It Company

Number of Pages Required

5+ page

Font styles to use
Sans Serif

Colors
3276b5
faa54b
0355a3
fac994

Requirements
Must have
• Ideally would use Wordpress theme (Divi for example or other)
• Very smart front end
• Will upload logo soon
• (Harlow Net Learning)
• harlownetlearning.edu.au
• Graphics of 'people' pretty important - with a variety of ages.
Nice to have
• Interesting page
• National presence
• A bit University looking
• Professional
• Graphics of people
• Blog
• Graphics of people
• Age range from job seekers, to business folk, etc

```html
<!DOCTYPE html>
<html lang="en">
<head>
<meta charset="utf-8">
<title>Harlow Net Learning</title>
<link href="https://fonts.googleapis.com/css2?family=Cinzel:wght@400;600&family=Raleway:wght@300;400;600;700;800&family=Lato:wght@300;400;700&display=swap" rel="stylesheet">
<style>
:root{
  --navy:#1c3a8e;
  --navy-deep:#162b6e;
  --teal:#2fbfd9;
  --yellow:#f6cf47;
  --orange:#f2a53c;
  --red:#e4533f;
  --ink:#1e1e1e;
  --text:#555;
  --muted:#888;
  --line:#e3e3e3;
  --slate:#2f3c4f;
  --footer:#1b1b1b;
}
*{box-sizing:border-box;margin:0;padding:0}
html,body{width:1200px;height:3093px;overflow:hidden}
body{position:relative;font-family:'Lato',sans-serif;color:var(--text);background:#fff}
.abs{position:absolute}

/* header */
.site-header{position:absolute;left:0;top:0;width:1200px;height:128px;background:#fff}
.brand{position:absolute;left:108px;top:52px;display:flex;align-items:center;gap:10px}
.brand-mark{width:26px;height:26px;background:var(--navy)}
.brand-name{font-family:'Cinzel',serif;font-weight:600;font-size:22px;color:var(--navy);letter-spacing:.5px}
.free-call{position:absolute;right:112px;top:30px;font-family:'Raleway',sans-serif;font-weight:800;font-size:18px;letter-spacing:1.5px;color:var(--ink)}
.main-nav{position:absolute;right:110px;top:74px;display:flex;height:38px}
.main-nav a{display:block;padding:0 13px;line-height:38px;font-family:'Raleway',sans-serif;font-size:10.5px;font-weight:600;color:#333;text-decoration:none;text-transform:uppercase}
.main-nav a.active{background:var(--navy);color:#fff;padding:0 20px}

/* hero */
.hero{position:absolute;left:0;top:128px;width:1200px;height:452px;background:linear-gradient(100deg,#6f8e99 0%,#a9b7b4 22%,#8aa3b0 45%,#c7a48c 62%,#d6dde2 80%,#e9eef0 100%)}
.hero-shade{position:absolute;inset:0;background:rgba(20,40,70,.18)}
.hero h1{position:absolute;left:0;width:1200px;top:164px;text-align:center;font-family:'Raleway',sans-serif;font-weight:700;font-size:42px;color:#fff}
.hero p{position:absolute;left:260px;width:680px;top:218px;text-align:center;font-size:12.5px;line-height:20px;color:#fff}
.search{position:absolute;left:118px;top:282px;display:flex;gap:4px;height:42px}
.field{background:#fff;height:42px;display:flex;align-items:center;justify-content:space-between;padding:0 14px;font-size:11.5px;color:#999}
.field svg{width:10px;height:10px}
.search-btn{width:156px;background:var(--teal);color:#fff;font-family:'Raleway',sans-serif;font-weight:700;font-size:11.5px;display:flex;align-items:center;justify-content:center;letter-spacing:.5px}

/* welcome */
.welcome-title{position:absolute;left:0;top:630px;width:1200px;text-align:center;font-family:'Cinzel',serif;font-size:35px;letter-spacing:2.5px;color:var(--ink)}
.welcome-title span{color:var(--navy)}
.welcome-copy{position:absolute;left:175px;width:850px;top:706px;text-align:center;font-size:12.5px;line-height:20px;color:#444}
.welcome-copy p+p{margin-top:20px}
.features{position:absolute;left:108px;top:868px;width:985px;display:flex}
.feature{flex:1;text-align:center;padding:0 12px}
.feature h3{font-family:'Raleway',sans-serif;font-weight:700;font-size:15px;color:var(--ink);text-transform:uppercase;margin-bottom:12px}
.feature p{font-size:11.5px;line-height:17px;color:var(--muted)}

/* students / why */
.section-head{font-family:'Raleway',sans-serif;font-size:28px;color:#333;font-weight:400}
.section-head b{font-weight:700}
.students{position:absolute;left:112px;top:1015px;width:460px}
.quote{position:relative;margin-top:26px;padding-left:30px;font-size:11.5px;line-height:20px;color:var(--muted)}
.quote::before{content:"\201C";position:absolute;left:4px;top:-6px;font-family:Georgia,serif;font-size:34px;font-weight:700;color:var(--red)}
.avatar{width:52px;height:52px;border-radius:50%;background:radial-gradient(circle at 50% 40%,#e8c7a8,#9bb8c9);margin:30px 0 0 40px}
.author{margin:18px 0 0 36px;font-size:10px;color:#999}
.pager{display:flex;gap:6px;margin:28px 0 0 36px}
.pager span{width:26px;height:26px;border:1px solid var(--line);display:flex;align-items:center;justify-content:center}
.why{position:absolute;left:618px;top:1015px;width:474px}
.accordion{margin-top:22px}
.acc-item{border:1px solid var(--line);margin-bottom:9px;box-shadow:0 1px 2px rgba(0,0,0,.05)}
.acc-head{height:40px;display:flex;align-items:center;justify-content:space-between;padding:0 20px 0 26px;font-family:'Raleway',sans-serif;font-size:10px;font-weight:600;text-transform:uppercase;color:#333}
.acc-head i{color:var(--red);font-style:normal;font-size:12px}
.acc-item.open .acc-head{color:var(--red)}
.acc-body{padding:4px 26px 20px;font-size:10.5px;line-height:21px;color:var(--muted);border-top:1px solid var(--line);padding-top:12px}

/* promo banners */
.promo{position:absolute;top:1420px;width:476px;height:205px;overflow:hidden}
.promo-teal{left:112px;background:var(--teal)}
.promo-yellow{left:613px;background:var(--yellow)}
.promo-art{position:absolute;top:0;height:205px}
.promo-teal .promo-art{left:0;width:250px;background:linear-gradient(135deg,#38c7df,#27adc6)}
.promo-yellow .promo-art{left:0;width:260px;background:linear-gradient(135deg,#f8d65e,#e9bf3c)}
.promo-text{position:absolute;right:26px;top:48px;text-align:right;color:#fff;font-family:'Raleway',sans-serif}
.promo-text strong{display:block;font-size:29px;font-weight:800;line-height:32px}
.promo-text em{display:block;font-style:normal;font-size:26px;font-weight:300;line-height:28px}
.promo-text hr{border:0;border-top:1px solid rgba(255,255,255,.6);width:230px;margin:12px 0 12px auto}
.promo-text small{font-size:12px;font-family:'Lato',sans-serif}

/* newsletter */
.newsletter{position:absolute;left:0;top:1680px;width:1200px;height:132px;background:var(--navy)}
.newsletter .icon{position:absolute;left:118px;top:40px;opacity:.35}
.newsletter .icon-front{position:absolute;left:176px;top:42px}
.news-text{position:absolute;left:228px;top:44px;color:#fff}
.news-text h4{font-family:'Raleway',sans-serif;font-weight:700;font-size:15px}
.news-text p{font-size:10.5px;color:#b9c4e4;margin-top:4px}
.news-form{position:absolute;left:632px;top:44px;display:flex;height:40px}
.news-input{width:340px;background:#fff;font-size:9.5px;color:#aaa;padding-left:16px;display:flex;align-items:center}
.news-btn{width:118px;background:var(--orange);color:#fff;font-size:9.5px;font-weight:700;display:flex;align-items:center;justify-content:center}

/* latest posts */
.posts-title{position:absolute;left:0;top:1870px;width:1200px;text-align:center;font-family:'Raleway',sans-serif;font-weight:700;font-size:21px;color:var(--ink)}
.posts-rule{position:absolute;left:112px;top:1930px;width:978px;border-top:1px solid var(--line)}
.posts-accent{position:absolute;left:587px;top:1926px;width:26px;height:5px;background:var(--orange)}
.post{position:absolute;top:1962px;width:310px}
.post-img{height:200px}
.post h5{margin-top:14px;font-family:'Raleway',sans-serif;font-weight:700;font-size:12.5px;line-height:18px;color:var(--ink)}
.post p{margin-top:6px;font-size:11.5px;line-height:17px;color:var(--muted)}
.post .bar{width:26px;height:3px;background:var(--orange);margin:10px 0 10px}
.post .meta{font-size:10px;color:#999;display:flex;align-items:center;gap:6px}
.post .meta b{color:var(--orange);font-weight:400;font-style:italic}
.side-post{position:absolute;left:780px;width:310px;display:flex;gap:14px}
.date{width:76px;height:76px;border-radius:50%;background:var(--yellow);display:flex;align-items:center;justify-content:center;flex:none}
.date span{width:56px;height:56px;border-radius:50%;background:var(--navy);color:var(--yellow);font-size:11px;line-height:13px;text-align:center;display:flex;flex-direction:column;justify-content:center;font-weight:700}
.side-post h6{font-family:'Raleway',sans-serif;font-weight:700;font-size:12.5px;line-height:17px;color:var(--ink);margin-top:4px}
.side-post p{font-size:11px;line-height:15px;color:var(--muted);margin-top:6px}

/* trusted */
.trusted{position:absolute;left:0;top:2356px;width:1200px;height:344px;background:var(--slate)}
.trusted h2{position:absolute;left:0;width:1200px;top:22px;text-align:center;font-family:'Raleway',sans-serif;font-weight:600;font-size:27px;color:#fff}
.partners{position:absolute;left:124px;top:98px;display:flex;gap:22px}
.partner{width:173px;height:90px;background:#fff;display:flex;align-items:center;justify-content:center;font-family:'Raleway',sans-serif;font-weight:700;font-size:22px;color:#222;border-bottom:4px solid var(--teal)}
.partner:nth-child(2){border-color:var(--orange)}
.partner:nth-child(3){border-color:var(--red)}
.partner:nth-child(4){border-color:var(--yellow)}
.trusted p{position:absolute;left:280px;width:640px;top:238px;text-align:center;font-size:9.5px;line-height:18px;color:#fff;text-transform:uppercase}

/* footer */
.site-footer{position:absolute;left:0;top:2700px;width:1200px;height:340px;background:var(--footer)}
.f-col{position:absolute;top:72px}
.f-col h4{font-family:'Cinzel',serif;font-weight:600;font-size:15px;color:#fff;letter-spacing:.5px;margin-bottom:20px}
.f-col li{list-style:none;font-size:11px;color:#bbb;line-height:34px}
.f-col li::before{content:"\203A";margin-right:8px;color:#ddd}
.insta{display:grid;grid-template-columns:repeat(3,62px);gap:9px}
.insta div{height:62px}
.contact-list p{font-size:11px;line-height:34px;color:#bbb}
.contact-list p.addr{line-height:22px;margin-bottom:6px}
.bottom-bar{position:absolute;left:0;top:3040px;width:1200px;height:53px;background:var(--navy-deep);text-align:center;line-height:53px;font-size:11px;color:#9aa5c8}
</style>
</head>
<body>

<header class="site-header">
  <div class="brand"><div class="brand-mark"></div><div class="brand-name">Harlow Net Learning</div></div>
  <div class="free-call">FREE CALL :- 1800 555 014</div>
  <nav class="main-nav">
    <a class="active">Home</a><a>About Us</a><a>Event</a><a>Blog</a><a>Course</a><a>Teacher</a><a>Gallery</a><a>Pages</a><a>Contact Us</a>
  </nav>
</header>

<section class="hero" role="img" aria-label="Students of different ages studying together at laptops in a bright classroom">
  <div class="hero-shade"></div>
  <h1>Harlow Net Learning</h1>
  <p>Harlow Net Learning is an Australian owned online training company delivering over 600 well priced, accessible short courses in a variety of skill sets online directly to you.</p>
  <div class="search">
    <div class="field" style="width:262px">Category <svg viewBox="0 0 10 10"><path d="M1 3l4 4 4-4" fill="none" stroke="#999" stroke-width="1.4"/></svg></div>
    <div class="field" style="width:271px">Course Status <svg viewBox="0 0 10 10"><path d="M1 3l4 4 4-4" fill="none" stroke="#999" stroke-width="1.4"/></svg></div>
    <div class="field" style="width:265px">Type Keyword</div>
    <div class="search-btn">SEARCH</div>
  </div>
</section>

<h2 class="welcome-title">WELCOME TO <span>HARLOW NET LEARNING</span></h2>
<div class="welcome-copy">
  <p>Harlow Net Learning is one of Australia's leading provider of flexible and affordable online continuing professional development programs, with over 600 online courses now available.</p>
  <p>Our range of self-paced online courses are delivered completely online via our e-learning system 24/7.<br>We offer a range of popular online courses in accounting, finance, bookkeeping, management, marketing, information technology, project management and more. Our online courses are industry relevant and are designed to help you achieve your career goals.</p>
</div>

<div class="features">
  <div class="feature"><h3>Online Courses</h3><p>Whether you stay with us for one week or one year, we will make sure you have the time of your life.</p></div>
  <div class="feature"><h3>Books &amp; Library</h3><p>Discover free online courses from top universities, and functionality of Kestrel, the that makes teaching.</p></div>
  <div class="feature"><h3>Great Teachers</h3><p>While other platforms offer only a subset of online teaching tools, network provides all the ease.</p></div>
  <div class="feature"><h3>Certification</h3><p>Whether you stay with us for one week or one year, we will make sure you have the time of your life.</p></div>
</div>

<section class="students">
  <h2 class="section-head">What <b>Students Say</b></h2>
  <p class="quote">Having years of Industry experience, he works on many project and at present he is providing Consultancy for many renowned IT companies. America in various industries to include a military finance organization.</p>
  <div class="avatar" role="img" aria-label="Portrait of the student giving the testimonial"></div>
  <div class="author">– Mr.Tavin @Designer</div>
  <div class="pager">
    <span><svg width="8" height="8" viewBox="0 0 8 8"><path d="M5 1L2 4l3 3" fill="none" stroke="#999"/></svg></span>
    <span><svg width="8" height="8" viewBox="0 0 8 8"><path d="M3 1l3 3-3 3" fill="none" stroke="#999"/></svg></span>
  </div>
</section>

<section class="why">
  <h2 class="section-head">Why <b>Harlow ?</b></h2>
  <div class="accordion">
    <div class="acc-item open">
      <div class="acc-head">Learn and get training from experts <i>&#9652;</i></div>
      <div class="acc-body">Fusce eleifend. Donec sapien sed phase lusa. Pellentesque lacus.Vivamus lorem arcu semper duiac. Cras ornare arcu vamus nda leo. Etiam ind arc morbi justo mauris tend pus pharetra interdum at congue semper purus.</div>
    </div>
    <div class="acc-item"><div class="acc-head">Enjoy our free online courses <i>-</i></div></div>
    <div class="acc-item"><div class="acc-head">Learn anytime &amp; anywhere <i>-</i></div></div>
    <div class="acc-item"><div class="acc-head">Basic to advance: we teach everything <i>-</i></div></div>
  </div>
</section>

<div class="promo promo-teal">
  <div class="promo-art" role="img" aria-label="Notebook and pencil on a desk"></div>
  <div class="promo-text"><strong>TRENDING</strong><em>COURSES</em><hr><small>Watch classes anytime, anywhere.</small></div>
</div>
<div class="promo promo-yellow">
  <div class="promo-art" role="img" aria-label="Smiling woman pointing at a laptop screen"></div>
  <div class="promo-text"><strong>NEW</strong><em>COURSES</em><hr><small>Create projects and build a portfolio.</small></div>
</div>

<section class="newsletter">
  <svg class="icon" width="70" height="52" viewBox="0 0 70 52"><rect x="1" y="1" width="68" height="50" fill="none" stroke="#fff" stroke-width="2"/><path d="M1 1l34 26L69 1" fill="none" stroke="#fff" stroke-width="2"/></svg>
  <svg class="icon-front" width="34" height="26" viewBox="0 0 34 26"><rect x="1" y="1" width="32" height="24" fill="none" stroke="#fff" stroke-width="2"/><path d="M1 1l16 12L33 1" fill="none" stroke="#fff" stroke-width="2"/></svg>
  <div class="news-text"><h4>Subscribe Our Newsletter</h4><p>Nulla feugiat nibh placerat fermentum rutrum ante risus euismod</p></div>
  <div class="news-form"><div class="news-input">YOUR EMAIL ADDRESS...</div><div class="news-btn">SUBSCRIBE</div></div>
</section>

<h2 class="posts-title">LATEST POSTS</h2>
<div class="posts-rule"></div>
<div class="posts-accent"></div>

<article class="post" style="left:112px">
  <div class="post-img" role="img" aria-label="Young woman holding up a smartphone" style="background:linear-gradient(135deg,#cfd8dc,#e9d3bd 60%,#b9c2c8)"></div>
  <h5>Learn the language of love, morbi venenatis lacinia</h5>
  <p>Education is the process of facilitating learning. Knowledge, skills, values, beliefs, and habits of a...</p>
  <div class="bar"></div>
  <div class="meta">2015-07-13 &nbsp; (4) &nbsp; by <b>admin</b></div>
</article>
<article class="post" style="left:446px">
  <div class="post-img" role="img" aria-label="Students reading at tables in a library" style="background:linear-gradient(135deg,#e9ecef,#f3e6cf 55%,#d8dde1)"></div>
  <h5>Learn English connect with the world</h5>
  <p>Education is the process of facilitating learning. Knowledge, skills, values, beliefs, and habits of a...</p>
  <div class="bar"></div>
  <div class="meta">2015-01-24 &nbsp; (0) &nbsp; by <b>admin</b></div>
</article>

<div class="side-post" style="top:1962px">
  <div class="date"><span>Nov<br>01</span></div>
  <div><h6>The Surprising Reason College Expensive</h6><p>Cras condimentum a elit eget sagittis. Ut dignissim sapien feugiat.</p></div>
</div>
<div class="side-post" style="top:2066px">
  <div class="date"><span>Nov<br>09</span></div>
  <div><h6>Now Chicago photography school</h6><p>Quisque tortor nisi, tristique sit amet commodo vel, commodo at.</p></div>
</div>
<div class="side-post" style="top:2170px">
  <div class="date"><span>Nov<br>14</span></div>
  <div><h6>Those Other College Expenses Thinking About</h6><p>Cras condimentum a elit eget sagittis. Ut dignissim sapien feugiat.</p></div>
</div>

<section class="trusted">
  <h2>Trusted By</h2>
  <div class="partners">
    <div class="partner">Corvella</div>
    <div class="partner">Brightmart</div>
    <div class="partner">Zentrosoft</div>
    <div class="partner">Quickhaul</div>
    <div class="partner">Aldmoor Aero</div>
  </div>
  <p>Halden Education Centre is one of the world's busiest public library systems, with over 10 million books, movies and other items to borrow. Upon successful completion receive a certificate showing your achievement for completing one of our rigorous classes.</p>
</section>

<footer class="site-footer">
  <div class="f-col" style="left:135px"><h4>INFORMATION</h4><ul><li>About Us</li><li>Our Stories</li><li>My Account</li><li>Our History</li><li>Sprcialist Info</li></ul></div>
  <div class="f-col" style="left:385px"><h4>STUDENT HELP</h4><ul><li>My Info</li><li>My Questions</li><li>F.A.Q</li><li>Serch Courses</li><li>Latest Informations</li></ul></div>
  <div class="f-col" style="left:636px"><h4>INSTAGRAM</h4>
    <div class="insta" role="img" aria-label="Grid of six campus and student photos">
      <div style="background:#6d8fa8"></div><div style="background:#b7a48f"></div><div style="background:#c9b9a8"></div>
      <div style="background:#7fa0b6"></div><div style="background:#a7b38f"></div><div style="background:#d0c3b4"></div>
    </div>
  </div>
  <div class="f-col contact-list" style="left:886px"><h4>CONTACT</h4>
    <p class="addr">Lorem ipsum dolor Brookvale,<br>Ohio, USA</p>
    <p>Phone : 5 (012) 4565 321</p>
    <p>Fax : 5 (012) 4565 987</p>
    <p>Email : info@harlownetlearning.edu.au</p>
  </div>
</footer>
<div class="bottom-bar">copyright@harlownetlearning.edu.au</div>

</body>
</html>
```